Tolvern landscape website

Our company is called Tolvern Landscape, Inc. We are located in Oak Bluffs, Martha's Vineyard Island, MA. We are a design construction maintenance firm offering a wide variety of services. We need to build a website for our Landscape, Construction, and Maintenance Company. The ability to interchange photos in many locations. 6-7 Tabs for individualized services. Ability to change and alter text. Use of our logo to increase branding. Modern, clean, simplified backgrounds are appealing. Possibly black background to allow the colors of flowers and logos to pop. Simplicity in management is of importance! The final design should lend itself to an upscale marketplace.
Updates

Dear Designers, Please be advised that the web design needs coding as well. Coding will not be charged on top of whatever investment and must be inclusive in the package. In short, you will not ask the client for more funds. -BriefHarbor Admin (Tomas Aldrete)

Target Market(s)

These are second homeowners. estate type properties. upscale clientele.

Industry/Entity Type

Construction

Requirements
Must have
• multiple tabs 6-7 to be able to highlight services. space for text and photos/albums. easy to navigate.
Should not have
• cheesy gimmicky cheap type feel

```html
<!DOCTYPE html>
<html lang="en">
<head>
<meta charset="utf-8">
<title>Tolvern Landscape</title>
<link href="https://fonts.googleapis.com/css2?family=Source+Sans+3:wght@400;600&display=swap" rel="stylesheet">
<style>
:root{
  --stage:#000;
  --page:#f2f2f2;
  --accent-red:#e3202b;
  --nav-gold:#f9b21b;
  --ink:#2b2b2b;
  --nav-ink:#3a2410;
  --brand-green:#2f7a3a;
  --caption-bg:#050505;
  --icon-ring:#bdbdbd;
}
*{box-sizing:border-box;margin:0;padding:0}
html,body{width:890px;height:1200px;overflow:hidden}
body{background:var(--stage);font-family:"Source Sans 3",sans-serif;color:var(--ink);position:relative}
.page{position:absolute;left:74px;top:26px;width:741px;height:1152px;background:var(--page);border-top:5px solid var(--accent-red);border-bottom:5px solid var(--accent-red);overflow:hidden}
.abs{position:absolute}
.nav-band{left:0;top:66px;width:741px;height:44px;background:var(--nav-gold)}
.nav{left:224px;top:79px;width:500px;height:20px;font-size:13px;color:var(--nav-ink)}
.nav span{position:absolute;top:0;white-space:nowrap}
.brand{left:23px;top:15px;width:125px;height:125px;border-radius:50%;background:var(--brand-green);border:4px solid #fff;box-shadow:0 0 0 1px #333;display:flex;align-items:center;justify-content:center;color:#fff;font-size:22px;font-weight:600;z-index:2}
.social{top:25px;left:435px;display:flex;gap:5px}
.social i{width:25px;height:25px;border-radius:50%;border:1px solid var(--icon-ring);background:#fafafa;display:block}
.call{left:591px;top:30px;font-size:13px;color:#222;white-space:nowrap}
.hero{left:0;top:110px;width:741px;height:339px;background:linear-gradient(180deg,#d9c98a 0%,#8a8b3e 25%,#4d6b2a 55%,#6b7a36 80%,#8a7a55 100%)}
.hero-caption{left:413px;top:288px;width:266px;height:40px;background:rgba(20,20,20,.82);color:#fff;font-size:24px;line-height:40px;text-align:center;white-space:nowrap}
.hero-arrows{left:22px;top:388px;display:flex;gap:2px}
.hero-arrows div{width:40px;height:42px;background:rgba(30,30,30,.75);display:flex;align-items:center;justify-content:center}
h2{font-weight:400;font-size:19px;line-height:22px;color:#333;white-space:nowrap}
.intro-title{left:14px;top:463px}
.intro-sub{left:15px;top:489px;font-size:14px;line-height:18px;color:#333;white-space:nowrap}
.body-text{font-size:9.6px;line-height:11.6px;color:#222;text-align:justify}
.intro-text{left:15px;top:517px;width:480px}
.btn{left:15px;top:580px;width:73px;height:25px;background:var(--accent-red);color:#fff;font-size:11px;line-height:25px;text-align:center;border-radius:2px}
.intro-photo{left:517px;top:463px;width:206px;height:122px;background:#ddd;padding:5px;box-shadow:0 8px 6px -6px rgba(0,0,0,.4)}
.intro-photo div{width:100%;height:100%;background:linear-gradient(135deg,#7a8a4a,#5f7f3a 40%,#c9b84a 60%,#5a4a8a)}
.service{top:624px;width:211px;height:200px}
.service h2{position:absolute;top:0;left:0}
.service .photo{position:absolute;top:28px;left:0;width:211px;height:108px}
.service h3{position:absolute;top:146px;left:4px;width:207px;font-weight:400;font-size:14px;line-height:18px;color:#333;white-space:nowrap}
.service p{position:absolute;top:173px;left:4px;width:206px}
.gallery-title{left:14px;top:850px}
.card{top:883px;width:150px;height:201px;box-shadow:0 8px 6px -6px rgba(0,0,0,.45)}
.card .photo{height:146px}
.card .cap{height:55px;background:var(--caption-bg);padding:6px 9px;color:#fff;font-size:9.6px;line-height:11.5px;text-align:justify}
.card .cap b{display:block;font-weight:400;color:var(--accent-red);font-size:10.5px;margin-bottom:3px;text-align:left;white-space:nowrap}
.zoom{left:40px;top:69px;display:flex;gap:4px}
.zoom i{width:30px;height:30px;border-radius:50%;background:#1a1a1a;display:flex;align-items:center;justify-content:center}
.footer-nav{left:22px;top:1106px;width:420px;height:14px;font-size:10px;color:#222}
.footer-nav span{position:absolute;top:0;white-space:nowrap}
.copy{right:18px;top:1107px;font-size:10px;color:#222;white-space:nowrap}
</style>
</head>
<body>
<div class="page">
  <div class="abs nav-band"></div>
  <div class="abs brand">Tolvern</div>
  <div class="abs social"><i></i><i></i><i></i><i></i><i></i></div>
  <div class="abs call">Call Us : 1800 . 555 . 914</div>
  <nav class="abs nav">
    <span style="left:0">Home</span>
    <span style="left:56px">Landscape</span>
    <span style="left:138px">Construction</span>
    <span style="left:231px">Maintenance</span>
    <span style="left:328px">About</span>
    <span style="left:386px">Blog</span>
    <span style="left:434px">Contact Us</span>
  </nav>

  <div class="abs hero" role="img" aria-label="Sunlit cottage garden with a gravel path, flowering beds and a small house"></div>
  <div class="abs hero-caption">Welcome To Tolvern</div>
  <div class="abs hero-arrows">
    <div><svg width="14" height="24" viewBox="0 0 14 24"><path d="M12 1 1 12l11 11" fill="none" stroke="#ddd" stroke-width="1.2"/></svg></div>
    <div><svg width="14" height="24" viewBox="0 0 14 24"><path d="M2 1l11 11L2 23" fill="none" stroke="#ddd" stroke-width="1.2"/></svg></div>
  </div>

  <h2 class="abs intro-title">Welcome to Our Website</h2>
  <div class="abs intro-sub">Duis aute irure dolor in reprehenderit in voluptate</div>
  <p class="abs body-text intro-text">Duis aute irure dolor in reprehenderit in voluptate velit esse cillum dolore eu fugiat nulla pariatur. Excepteur sint occaecat cupidatat non proident, sunt in culpa qui officia deserunt mollit anim id est laborum velit esse cillum dolore eu fugiat nulla pariatur. Excepteur sint occaecat cupidatat non proident, sunt in culpa qui officia deserunt mollit anim id est laborum</p>
  <div class="abs btn">Read more</div>
  <div class="abs intro-photo"><div role="img" aria-label="Stone garden steps lined with yellow and purple flowers"></div></div>

  <section class="abs service" style="left:18px">
    <h2>Landscape</h2>
    <div class="photo" role="img" aria-label="Curved paver walkway beside a stone wall and lush planting" style="background:linear-gradient(135deg,#4e6a3a,#3d7a2a 50%,#8fc23a)"></div>
    <h3>Duis aute irure dolor</h3>
    <p class="body-text">Duis aute irure dolor in reprehenderit in voluptate velit esse cillum dolore eu fugiat nulla pariatur.</p>
  </section>
  <section class="abs service" style="left:263px">
    <h2>Construction</h2>
    <div class="photo" role="img" aria-label="Worker repairing a dark shingle roof" style="background:linear-gradient(160deg,#8a8a8a,#2e3c55 45%,#1c2538)"></div>
    <h3>Duis aute irure dolor</h3>
    <p class="body-text">Duis aute irure dolor in reprehenderit in voluptate velit esse cillum dolore eu fugiat nulla pariatur.</p>
  </section>
  <section class="abs service" style="left:509px">
    <h2>Maintenance</h2>
    <div class="photo" role="img" aria-label="Brick garden path between low stone walls and a lawn" style="background:linear-gradient(180deg,#8fb0c8,#4f7a3a 40%,#7a6a55 80%)"></div>
    <h3>Duis aute irure dolor</h3>
    <p class="body-text">Duis aute irure dolor in reprehenderit in voluptate velit esse cillum dolore eu fugiat nulla pariatur.</p>
  </section>

  <h2 class="abs gallery-title">Photo Gallery</h2>
  <div class="abs card" style="left:15px">
    <div class="photo" role="img" aria-label="Shingled estate house with a flagpole under blue sky" style="background:linear-gradient(180deg,#3a6fc0,#8fb0d8 45%,#4a4030 75%,#6a5a3a)"></div>
    <div class="cap"><b>Landscape Construction</b>Duis aute irure dolor in reprehenderit.</div>
    <div class="abs zoom">
      <i><svg width="16" height="16" viewBox="0 0 16 16"><circle cx="7" cy="7" r="5" fill="none" stroke="#fff" stroke-width="1.6"/><path d="M10.5 10.5 15 15M7 4.5v5M4.5 7h5" stroke="#fff" stroke-width="1.6"/></svg></i>
      <i><svg width="16" height="16" viewBox="0 0 16 16"><path d="M6.5 9.5l3-3M5 8 3 10a2.1 2.1 0 0 0 3 3l2-2M11 8l2-2a2.1 2.1 0 0 0-3-3L8 5" fill="none" stroke="#fff" stroke-width="1.6"/></svg></i>
    </div>
  </div>
  <div class="abs card" style="left:202px">
    <div class="photo" role="img" aria-label="Snow-covered field by the water under clear blue sky" style="background:linear-gradient(180deg,#1f4fa8,#6f97d0 55%,#f4f6fa 70%,#e6eaf0)"></div>
    <div class="cap"><b>Landscape Construction</b>Duis aute irure dolor in reprehenderit.</div>
  </div>
  <div class="abs card" style="left:388px">
    <div class="photo" role="img" aria-label="Bare tree over a snowy shoreline" style="background:linear-gradient(180deg,#2a5fb0,#8aa8d0 50%,#eef1f5 65%,#dde3ea)"></div>
    <div class="cap"><b>Landscape Construction</b>Duis aute irure dolor in reprehenderit.</div>
  </div>
  <div class="abs card" style="left:574px">
    <div class="photo" role="img" aria-label="White cottage behind a wide green lawn and trees" style="background:linear-gradient(180deg,#2e3a28,#4a5a3a 40%,#2f5a24 70%,#1f4a18)"></div>
    <div class="cap"><b>Landscape Construction</b>Duis aute irure dolor in reprehenderit.</div>
  </div>

  <nav class="abs footer-nav">
    <span style="left:0">Home</span>
    <span style="left:46px">Landscape</span>
    <span style="left:112px">Construction</span>
    <span style="left:188px">Maintenance</span>
    <span style="left:268px">About</span>
    <span style="left:314px">Blog</span>
    <span style="left:353px">Contact Us</span>
  </nav>
  <div class="abs copy">© 2014.www.tolvernsite.com</div>
</div>
</body>
</html>
```